Business Cards and Stationery for Brook Harlow Supply & Advisory sàrl
Simple
Karim Ait Lounes
Associé gérant
CP 7148
CH-1002 Lausanne
Switzerland
kal@brookharlow.ch
www.brookharlow.ch
Business cards to look fresh, in alignment with logo branding.
Colour scheme, images and writting to coordinate with logo.
We may soon need to change our office address and, possibly add phone and fax numbers, so we need to use a font that I can modify.
We want to use the logo designed through Tessavane.

```html
<!DOCTYPE html>
<html lang="fr">
<head>
<meta charset="utf-8">
<title>Brook Harlow Supply &amp; Advisory sàrl — Carte de visite</title>
<link rel="stylesheet" href="https://fonts.googleapis.com/css2?family=Alegreya+Sans+SC:wght@400;500&display=swap">
<style>
  :root {
    --page: #e9e9e6;
    --card: #ffffff;
    --green: #3fa535;
    --green-light: #8cc63f;
    --teal: #2bb39a;
    --ink: #4a4a4a;
    --muted: #7a7a7a;
    --wash: #eef6ee;
    --shadow: rgba(0, 0, 0, 0.18);
  }
  html, body {
    margin: 0;
    width: 1200px;
    height: 900px;
    overflow: hidden;
    background: var(--page);
  }
  body {
    display: flex;
    align-items: center;
    justify-content: center;
    font-family: "Alegreya Sans SC", "Helvetica Neue", Arial, sans-serif;
  }
  .business-card {
    position: relative;
    width: 1000px;
    height: 620px;
    background: var(--card);
    box-shadow: 0 10px 30px var(--shadow);
    overflow: hidden;
  }
  .card-watermark {
    position: absolute;
    left: 40px;
    top: 150px;
    width: 370px;
    height: 370px;
    border-radius: 50%;
    background: radial-gradient(circle at 40% 35%, #f3f9f3 0%, var(--wash) 70%, #e4f1e6 100%);
  }
  .brand {
    position: absolute;
    left: 440px;
    top: 62px;
    display: flex;
    align-items: center;
    gap: 18px;
  }
  .brand-dot {
    width: 96px;
    height: 96px;
    border-radius: 50%;
    background: var(--green);
    flex: none;
  }
  .brand-name {
    color: var(--green);
    font-weight: 500;
    line-height: 1;
  }
  .brand-name .brand-main {
    display: block;
    font-size: 60px;
    letter-spacing: 1px;
  }
  .brand-name .brand-sub {
    display: block;
    font-size: 22px;
    letter-spacing: 3px;
    margin-top: 8px;
  }
  .contact-list {
    position: absolute;
    right: 46px;
    top: 300px;
    margin: 0;
    padding: 0;
    list-style: none;
    color: var(--ink);
    font-size: 21px;
    letter-spacing: 2px;
    line-height: 30px;
  }
  .contact-list li {
    display: flex;
    justify-content: flex-end;
    align-items: center;
    gap: 6px;
  }
  .contact-icon {
    width: 16px;
    height: 16px;
    flex: none;
  }
  .holder {
    position: absolute;
    left: 44px;
    bottom: 78px;
  }
  .holder-name {
    margin: 0;
    color: var(--teal);
    font-size: 30px;
    font-weight: 400;
    letter-spacing: 3px;
  }
  .holder-role {
    margin: 2px 0 0;
    color: var(--muted);
    font-size: 21px;
    letter-spacing: 3px;
  }
</style>
</head>
<body>
  <article class="business-card">
    <div class="card-watermark" aria-hidden="true"></div>

    <header class="brand">
      <span class="brand-dot" aria-hidden="true"></span>
      <span class="brand-name">
        <span class="brand-main">Brook Harlow</span>
        <span class="brand-sub">Supply &amp; Advisory sàrl</span>
      </span>
    </header>

    <ul class="contact-list">
      <li>CP 7148 CH-1002
        <svg class="contact-icon" viewBox="0 0 16 16" aria-hidden="true"><circle cx="8" cy="8" r="8" fill="var(--green)"/><path d="M8 3.5a3 3 0 0 0-3 3c0 2.2 3 6 3 6s3-3.8 3-6a3 3 0 0 0-3-3z" fill="#fff"/></svg>
      </li>
      <li>Lausanne Switzerland
        <svg class="contact-icon" viewBox="0 0 16 16" aria-hidden="true"><circle cx="8" cy="8" r="8" fill="var(--green-light)"/><path d="M4 8l3 3 5-6" stroke="#fff" stroke-width="1.8" fill="none"/></svg>
      </li>
      <li>+41 21 634 52 07
        <svg class="contact-icon" viewBox="0 0 16 16" aria-hidden="true"><circle cx="8" cy="8" r="8" fill="var(--green)"/><path d="M5.2 4.2l1.6-.4 1 2-1 .8a5 5 0 0 0 2.6 2.6l.8-1 2 1-.4 1.6c-3.6.2-6.8-3-6.6-6.6z" fill="#fff"/></svg>
      </li>
      <li>+41 76 542 18 30
        <svg class="contact-icon" viewBox="0 0 16 16" aria-hidden="true"><circle cx="8" cy="8" r="8" fill="var(--green-light)"/><rect x="5.5" y="3.5" width="5" height="9" rx="1" fill="#fff"/></svg>
      </li>
      <li>+41 21 634 52 08
        <svg class="contact-icon" viewBox="0 0 16 16" aria-hidden="true"><circle cx="8" cy="8" r="8" fill="var(--green)"/><rect x="4" y="6" width="8" height="5" fill="#fff"/><rect x="5.5" y="4" width="5" height="2" fill="#fff"/></svg>
      </li>
      <li>kal@brookharlow.ch
        <svg class="contact-icon" viewBox="0 0 16 16" aria-hidden="true"><circle cx="8" cy="8" r="8" fill="var(--green-light)"/><rect x="4" y="5" width="8" height="6" fill="#fff"/><path d="M4 5l4 3.5L12 5" stroke="var(--green-light)" stroke-width="1" fill="none"/></svg>
      </li>
      <li>www.brookharlow.ch
        <svg class="contact-icon" viewBox="0 0 16 16" aria-hidden="true"><circle cx="8" cy="8" r="8" fill="var(--green)"/><circle cx="8" cy="8" r="4" stroke="#fff" stroke-width="1.2" fill="none"/><path d="M4 8h8M8 4v8" stroke="#fff" stroke-width="1"/></svg>
      </li>
    </ul>

    <footer class="holder">
      <p class="holder-name">Karim Ait Lounes</p>
      <p class="holder-role">Associé gérant</p>
    </footer>
  </article>
</body>
</html>
```